Letter head incorporating Our values and our Clover & Kite logo

here are our current letterheads, similar look and feel but incorporating our values logo too.
I have attached some of our flyers to give an idea of our look and feel of our brand

```html
<!DOCTYPE html>
<html lang="en">
<head>
<meta charset="utf-8">
<title>Clover &amp; Kite Letterhead</title>
<link rel="stylesheet" href="https://fonts.googleapis.com/css2?family=Poppins:wght@600;700;800&display=swap">
<style>
  :root {
    --brand-blue: #1fa3e0;
    --sky-light: #8fd3f4;
    --navy: #14284b;
    --sunny: #ffe41f;
    --leaf: #5cbf2a;
    --coral: #e8452c;
    --orange: #f7941d;
    --paper: #ffffff;
  }
  * { margin: 0; padding: 0; box-sizing: border-box; }
  html, body { width: 849px; height: 1200px; overflow: hidden; background: var(--paper); }
  body { font-family: "Poppins", sans-serif; color: var(--navy); }
  .letterhead { position: relative; width: 849px; height: 1200px; overflow: hidden; background: var(--paper); }

  .brand-panel {
    position: absolute; left: 0; top: 0; width: 256px; height: 268px;
    background: var(--brand-blue); border-bottom-right-radius: 34px;
    display: flex; flex-direction: column; align-items: center; justify-content: center; gap: 14px;
  }
  .brand-mark { width: 58px; height: 58px; border-radius: 50%; background: var(--sunny); }
  .brand-name { font-weight: 800; font-size: 30px; color: var(--paper); letter-spacing: 0.5px; }

  .corner-flags { position: absolute; right: 0; top: 0; }

  .contact-list {
    position: absolute; right: 40px; top: 86px; list-style: none; text-align: right;
    font-weight: 700; font-size: 16.5px; line-height: 24px;
  }
  .contact-list li { display: flex; justify-content: flex-end; align-items: center; gap: 9px; }
  .contact-list li::after {
    content: ""; width: 10px; height: 10px; border-radius: 50%; background: var(--brand-blue);
  }
  .contact-list .contact-address { color: var(--brand-blue); }

  .footer-band { position: absolute; left: 0; bottom: 0; }

  .values-badge {
    position: absolute; left: 652px; top: 948px; width: 184px;
  }
  .values-title {
    height: 76px; background: var(--brand-blue); border-radius: 18px 18px 0 0;
    display: flex; align-items: center; justify-content: center;
    font-weight: 800; font-size: 30px; color: var(--paper);
  }
  .values-list { list-style: none; background: var(--paper); padding: 8px 10px; }
  .values-list li {
    display: flex; align-items: center; gap: 7px;
    font-weight: 700; font-size: 9px; line-height: 17px; color: var(--navy);
  }
  .values-list li::before { content: ""; width: 12px; height: 12px; background: var(--swatch); }

  .site-address {
    position: absolute; left: 72px; top: 1140px;
    font-weight: 700; font-size: 27px; color: var(--navy);
  }
</style>
</head>
<body>
<main class="letterhead">
  <header>
    <div class="brand-panel">
      <span class="brand-mark"></span>
      <span class="brand-name">Clover &amp; Kite</span>
    </div>

    <svg class="corner-flags" width="150" height="70" viewBox="0 0 150 70" aria-hidden="true">
      <polygon points="18,22 56,22 40,52" fill="var(--leaf)"/>
      <polygon points="56,0 96,0 76,34" fill="var(--sunny)"/>
      <polygon points="86,14 124,14 106,48" fill="var(--coral)"/>
      <polygon points="114,0 150,0 150,32" fill="var(--brand-blue)"/>
    </svg>

    <ul class="contact-list">
      <li>(02) 5550 1234</li>
      <li>0400 555 218</li>
      <li>lilyfield@cloverandkite.edu.au</li>
      <li class="contact-address">27 Garden Lane, LILYFIELD NSW 2040</li>
    </ul>
  </header>

  <footer>
    <svg class="footer-band" width="849" height="260" viewBox="0 0 849 260" aria-hidden="true">
      <path d="M0,260 L0,240 C260,200 560,110 849,60 L849,260 Z" fill="var(--sky-light)"/>
      <path d="M0,260 L0,250 C300,215 580,140 849,100 L849,260 Z" fill="var(--sunny)"/>
      <path d="M0,260 L0,256 C320,230 600,170 849,145 L849,260 Z" fill="var(--paper)" opacity="0"/>
      <polygon points="0,150 46,150 22,188" fill="var(--leaf)"/>
      <polygon points="22,170 62,178 36,212" fill="var(--brand-blue)"/>
      <polygon points="0,196 34,206 0,236" fill="var(--orange)"/>
    </svg>

    <section class="values-badge" aria-label="Our Values">
      <div class="values-title">Our Values</div>
      <ul class="values-list">
        <li style="--swatch: var(--coral)">WE LEARN TOGETHER</li>
        <li style="--swatch: var(--leaf)">INNOVATE EDUCATION</li>
        <li style="--swatch: var(--brand-blue)">SAFETY FIRST</li>
        <li style="--swatch: var(--sunny)">EMPOWER CONNECTIONS</li>
      </ul>
    </section>

    <p class="site-address">cloverandkite.edu.au</p>
  </footer>
</main>
</body>
</html>
```